Investment fund website overhaul for modern aesthetic (example sites in description)

I would like to request an overhaul of our current website (www.silvercrestharborventures.com), which craftlayout.com builders initially designed. The goal is to update the site's look and functionality while maintaining most of the existing page structure. Specifically, I'd like to implement the following changes:

Visual Redesign:
Please redesign the site to more closely resemble the style and aesthetic of the following three websites:
https://www.veridane.com/
https://www.tbx.com/
https://coastlinebackers.com/

New Portfolio, Meet the team, News & Insights:
Add a new "Portfolio" page to showcase our acquired businesses and properties. As we currently don't have any acquisitions, please include a "Coming Soon" message or placeholder content that explains our acquisition strategy and future plans.

Client Portal (a log in function):
Implement a secure client portal with the following features:
User authentication (username and password)
Ability for us to assign login credentials to investors
A personalized dashboard for each investor, displaying:
Their investments (API to come in the next several months)
Relevant legal documents
Personal information
Payment transfer (ACH/Wire/crypto)

Existing Pages:
Maintain the current site structure and content for existing pages but update their design to match the new aesthetic from those 3 websites.
Potentially change the names and additional pages (Who we are, What we do, Meet the Team, Our portfolio, News & Insights and then a separate client portal tab that sends them to a login in screen)

Please provide an estimate for these changes and a proposed timeline for completion. If you have any questions or need further clarification, please don't hesitate to ask.

Target Market(s)

Investors

Industry/Entity Type

AI, blockchain, digital assets, finance, and banking

Coding

Coded - Design and coding required

Number of Pages Required

5+ page

Colors

Designer to choose colors to be used in the design.

Requirements
Must have
• Pages: Who we are (landing/home page); What we do (mission page; Meet the team (coming soon); and Portfolio (Content coming soon)
Nice to have
• Client portal would be nice to have, but a simple but with the option and login credential page is fine for the time being.

```html
<!DOCTYPE html>
<html lang="en">
<head>
<meta charset="utf-8">
<title>Silvercrest Harbor Ventures</title>
<link href="https://fonts.googleapis.com/css2?family=Kurale&family=Mulish:wght@400;600;700&display=swap" rel="stylesheet">
<style>
:root{
  --navy:#0b2341;
  --gold:#b8914a;
  --gold-dark:#a97f3a;
  --gold-light:#d7b878;
  --cream:#fdf5e4;
  --cream-soft:#fbf3e6;
  --grey-card:#eef0f3;
  --hero-bg:#f4f4f4;
  --ink:#1b1b1b;
  --muted:#666;
  --white:#fff;
}
*{box-sizing:border-box;margin:0;padding:0}
html,body{width:1200px;height:3945px;overflow:hidden}
body{position:relative;background:var(--white);font-family:'Mulish',sans-serif;color:var(--ink)}
.abs{position:absolute}
.serif{font-family:'Kurale',serif;font-weight:400}
.btn{position:absolute;display:flex;align-items:center;justify-content:center;font-size:14px;font-weight:600;letter-spacing:.5px;color:var(--white);border-radius:3px;text-transform:uppercase}
.btn-gold{background:var(--gold)}
.btn-navy{background:var(--navy)}
.top-rule{position:absolute;left:0;top:0;width:1200px;height:3px;background:var(--gold)}
.dot{position:absolute;border-radius:50%;background:var(--navy)}

/* Header */
.hero{position:absolute;left:0;top:3px;width:1200px;height:637px;background:linear-gradient(180deg,var(--hero-bg),#fafafa 80%,#fff)}
.brand{position:absolute;display:flex;align-items:center;gap:12px}
.brand-mark{width:46px;height:46px;background:var(--gold)}
.brand-name{font-family:'Kurale',serif;font-size:16px;line-height:17px;color:var(--navy);letter-spacing:.5px;text-transform:uppercase}
.nav{position:absolute;top:86px;left:430px;display:flex;gap:36px;font-size:13px;font-weight:600;color:var(--navy);letter-spacing:.5px}
.hero-art{position:absolute;left:505px;top:90px;width:695px;height:520px;border-radius:45% 40% 35% 50%;background:radial-gradient(ellipse at 55% 45%,#f0ece0 0%,#e8e2d2 40%,rgba(240,238,232,0) 72%)}
.hero-art-accent{position:absolute;left:1080px;top:70px;width:140px;height:240px;border-radius:50%;background:radial-gradient(ellipse,#e3b39b 0%,rgba(227,179,155,0) 70%)}
.hero-title{position:absolute;left:112px;top:228px;font-size:58px;line-height:72px;color:var(--ink)}

/* Growth */
.center{position:absolute;left:0;width:1200px;text-align:center}
.h2{font-size:42px;line-height:62px;color:var(--ink)}
.rule{position:absolute;height:2px;background:linear-gradient(90deg,rgba(184,145,74,0),var(--gold),rgba(184,145,74,0))}
.lead{font-size:17px;line-height:36px;color:var(--muted)}
.goal-card{position:absolute;top:1003px;width:423px;height:263px;border-radius:22px;text-align:center}
.goal-card .icon{position:absolute;left:173px;top:58px;width:76px;height:76px;border-radius:50%;display:flex;align-items:center;justify-content:center}
.goal-card p{position:absolute;left:40px;right:40px;top:152px;font-size:15.5px;line-height:31px;color:var(--muted)}

/* About band */
.about{position:absolute;left:0;top:1382px;width:1200px;height:628px;background:radial-gradient(circle at 30% 50%,#c5852f 0%,#c2863a 35%,#b98f48 70%,#c09a52 100%)}
.about-photo{position:absolute;left:89px;top:80px;width:508px;height:467px}
.about h3{position:absolute;left:655px;top:92px;font-size:46px;line-height:61px;color:var(--white)}
.about .line{position:absolute;left:655px;top:230px;width:337px;height:2px;background:rgba(255,255,255,.75)}
.about .text{position:absolute;left:655px;top:260px;width:440px;font-size:14.5px;line-height:29px;color:var(--white)}
.about .text p+p{margin-top:29px}

/* Provide */
.provide-card{position:absolute;top:2316px;width:316px;height:259px}
.provide-card .frame{position:absolute;inset:0;border:1.5px solid var(--navy);border-right-width:1.5px}
.provide-card .body{position:absolute;left:14px;top:14px;right:14px;bottom:14px;background:var(--cream-soft)}
.provide-card h4{position:absolute;left:42px;top:110px;font-family:'Kurale',serif;font-weight:400;font-size:25px;color:var(--ink)}
.provide-card p{position:absolute;left:42px;top:150px;width:235px;font-size:13px;line-height:24px;color:#777}
.provide-card svg{position:absolute;left:42px;top:44px}
.provide-card.featured .frame{border:none;background:var(--navy)}
.provide-card.featured .body{left:15px;top:15px;right:15px;bottom:15px;background:linear-gradient(135deg,#a6803e,#8f6e36)}
.provide-card.featured h4,.provide-card.featured p{color:var(--white)}

/* Invest */
.invest{position:absolute;left:0;top:2792px;width:1200px;height:840px;background:radial-gradient(ellipse at 50% 30%,#12315a 0%,var(--navy) 60%)}
.invest .title{font-size:46px;color:var(--white)}
.invest .para{font-size:15.5px;line-height:32px;color:var(--white)}
.newsletter{position:absolute;left:112px;top:412px;width:975px;height:329px;border-radius:60px;background:linear-gradient(100deg,#c08a3c,#c9a257 55%,#b58c44)}
.newsletter .horse{position:absolute;left:85px;top:35px;width:250px;height:260px;border-radius:30px;background:radial-gradient(ellipse,rgba(11,35,65,.85) 0%,rgba(11,35,65,.35) 55%,rgba(11,35,65,0) 72%)}
.newsletter h3{position:absolute;left:388px;top:42px;font-size:44px;line-height:53px;color:var(--white)}
.newsletter .input{position:absolute;left:390px;top:164px;width:487px;height:60px;background:var(--white);border-radius:4px;font-size:15px;color:#888;display:flex;align-items:center;padding-left:30px}

/* Footer */
.footer-links{position:absolute;top:3798px;left:0;width:1200px;display:flex;justify-content:center;gap:26px;font-size:14px;font-weight:600;color:var(--navy)}
.footer-links .sep{color:var(--navy);font-weight:400}
.social{position:absolute;top:3846px;left:0;width:1200px;display:flex;justify-content:center;gap:12px}
.social span{width:40px;height:40px;border-radius:50%;background:linear-gradient(135deg,var(--gold-light),var(--gold))}
.copy{position:absolute;top:3903px;left:0;width:1200px;text-align:center;font-size:11px;color:#555}
</style>
</head>
<body>
<div class="hero">
  <div class="hero-art" role="img" aria-label="Abstract flowing cream and gold ribbon sculpture"></div>
  <div class="hero-art-accent" role="img" aria-label="Soft peach ribbon accent"></div>
</div>
<div class="top-rule"></div>

<header>
  <div class="brand" style="left:89px;top:43px">
    <span class="brand-mark"></span>
    <span class="brand-name">Silvercrest Harbor<br>Ventures, LLC</span>
  </div>
  <nav class="nav">
    <span>WHO WE ARE</span><span>WHAT WE DO</span><span>OUR TEAM</span><span>OUR PORTFOLIO</span><span>NEWS &amp; INSIGHTS</span>
  </nav>
  <div class="btn btn-navy" style="left:946px;top:34px;width:141px;height:34px;font-size:12px">CLIENT PORTAL</div>
</header>

<span class="dot" style="left:42px;top:173px;width:15px;height:15px"></span>
<span class="dot" style="left:1090px;top:348px;width:15px;height:15px;background:var(--gold)"></span>
<span class="dot" style="left:581px;top:568px;width:15px;height:15px"></span>

<h1 class="hero-title serif">Where Technology<br>Meets Strategic<br>Investment</h1>
<div class="btn btn-gold" style="left:110px;top:476px;width:156px;height:46px">GET STARTED</div>

<span class="dot" style="left:-42px;top:655px;width:80px;height:80px"></span>
<div class="center h2 serif" style="top:717px">Driving Economic Growth Through<br>Strategic Acquisitions</div>
<div class="rule" style="left:470px;top:864px;width:260px"></div>
<div class="center lead" style="top:894px">Our strategy targets companies with stable growth potential that are resilient to market disruptions and<br>poised to leverage technological advancements in AI and blockchain.</div>

<div class="goal-card" style="left:159px;background:var(--cream)">
  <div class="icon" style="background:var(--gold)">
    <svg width="36" height="32" viewBox="0 0 36 32" fill="none" stroke="#fff" stroke-width="2.5"><path d="M3 18l9-8 7 6 12-12"/><path d="M24 4h7v7"/><path d="M5 30v-6M12 30v-10M19 30v-8M26 30v-12"/></svg>
  </div>
  <p>Targeting High-Potential Industries for Growth</p>
</div>
<div class="goal-card" style="left:619px;background:var(--grey-card)">
  <div class="icon" style="background:var(--navy)">
    <svg width="36" height="36" viewBox="0 0 36 36" fill="none" stroke="#fff" stroke-width="2"><circle cx="18" cy="8" r="4"/><circle cx="8" cy="12" r="3"/><circle cx="28" cy="12" r="3"/><path d="M18 12v8M8 15l5 5M28 15l-5 5"/><path d="M10 22h16l-2 9H12z" fill="#fff"/></svg>
  </div>
  <p>Scaling and Optimizing Business Operations for Long-Term Returns</p>
</div>
<span class="dot" style="left:1160px;top:1245px;width:80px;height:95px;background:none;border:2px solid var(--gold);box-shadow:inset 0 0 0 8px #fff, inset 0 0 0 40px var(--navy)"></span>

<section class="about">
  <svg class="about-photo" viewBox="0 0 508 467" role="img" aria-label="Photo of three colleagues reviewing documents together in an office">
    <path d="M150 20 C280 -10 400 10 480 130 C530 210 500 340 400 410 C300 480 160 470 80 400 C10 340 0 220 40 120 C70 60 110 30 150 20Z" fill="#0b2341"/>
    <path d="M140 30 C260 10 380 40 460 150 C500 220 480 330 390 395 C290 460 160 455 90 390 C25 330 15 220 50 130 C80 70 110 40 140 30Z" fill="#c6b49a" stroke="#c89a50" stroke-width="4"/>
  </svg>
  <h3 class="serif">Silvercrest Harbor<br>Ventures</h3>
  <div class="line"></div>
  <div class="text">
    <p>At Silvercrest Harbor Ventures, LLC, we are poised to revolutionize industries by leveraging cutting-edge AI and blockchain technologies.</p>
    <p>With a bold vision and resilience, we are ready to drive transformative growth and capture unparalleled opportunities in the market.</p>
  </div>
  <div class="btn btn-navy" style="left:655px;top:485px;width:135px;height:41px">READ MORE</div>
</section>

<span class="dot" style="left:52px;top:2093px;width:102px;height:102px;background:#e6e8eb;border:8px solid #f5f6f7"></span>
<div class="center serif" style="top:2100px;font-size:44px;color:var(--ink)">What We Provide</div>
<div class="rule" style="left:470px;top:2182px;width:260px"></div>
<div class="center" style="top:2212px;font-size:14px;line-height:32px;color:var(--muted)">Sed ut perspiciatis unde omnis iste natus error sit voluptatem accusantium doloremque laudantium, totam rem<br>aperiam, eaque ipsa quae ab illo inventore veritatis et quasi architecto beatae vitae dicta sunt</div>

<div class="provide-card" style="left:98px">
  <div class="frame"></div><div class="body"></div>
  <svg width="40" height="44" viewBox="0 0 40 44" fill="#b8914a"><circle cx="20" cy="12" r="10"/><path d="M4 44c0-12 7-20 16-20s16 8 16 20z"/></svg>
  <h4>Cybersecurity</h4>
  <p>Americans and their small to medium-sized businesses are highly vulnerable to increasing</p>
</div>
<div class="provide-card featured" style="left:442px">
  <div class="frame"></div><div class="body"></div>
  <svg width="44" height="44" viewBox="0 0 44 44" fill="none" stroke="#fff" stroke-width="2.5"><path d="M22 4l16 9v18l-16 9-16-9V13z"/><path d="M22 4v36M6 13l32 18M38 13L6 31"/></svg>
  <h4>Digital Assets</h4>
  <p>Treasury assets should actively work for the company rather than sit idle. SHV leverages Corecoin</p>
</div>
<div class="provide-card" style="left:787px">
  <div class="frame"></div><div class="body"></div>
  <svg width="46" height="44" viewBox="0 0 46 44" fill="#b8914a"><rect x="2" y="16" width="16" height="28"/><rect x="18" y="4" width="22" height="40"/><g fill="#fbf3e6"><rect x="6" y="22" width="4" height="4"/><rect x="6" y="32" width="4" height="4"/><rect x="23" y="10" width="4" height="4"/><rect x="31" y="10" width="4" height="4"/><rect x="23" y="20" width="4" height="4"/><rect x="31" y="20" width="4" height="4"/><rect x="23" y="30" width="4" height="4"/><rect x="31" y="30" width="4" height="4"/></g></svg>
  <h4>Commercial Real Estate</h4>
  <p>The growing demand for both physical and data storage solutions presents a significant challenge.</p>
</div>

<div class="btn btn-navy" style="left:455px;top:2635px;width:136px;height:41px">VIEW MORE</div>
<div class="btn btn-gold" style="left:609px;top:2635px;width:135px;height:41px">CONTACT US</div>
<span class="dot" style="left:1105px;top:2705px;width:34px;height:34px"></span>

<section class="invest">
  <div class="center serif title" style="top:85px">Invest In Your Future Today</div>
  <div class="rule" style="left:470px;top:170px;width:260px"></div>
  <div class="center para" style="top:197px">Discover high-potential investment opportunities in the Cybersecurity, Trade &amp; Construction Services, and<br>Specialized CRE industries.</div>
  <div class="btn btn-gold" style="left:533px;top:294px;width:135px;height:42px">CONTACT US</div>
  <div class="newsletter">
    <div class="horse" role="img" aria-label="Navy silhouette of a standing horse"></div>
    <h3 class="serif">Subscribe To Our Monthly<br>Newsletter</h3>
    <div class="input">Enter Email Address</div>
    <div class="btn btn-navy" style="left:390px;top:244px;width:172px;height:39px">SUBSCRIBE NOW</div>
  </div>
</section>

<footer>
  <span class="dot" style="left:61px;top:3720px;width:24px;height:24px"></span>
  <div class="brand" style="left:463px;top:3710px">
    <span class="brand-mark"></span>
    <span class="brand-name">Silvercrest Harbor<br>Ventures, LLC</span>
  </div>
  <div class="footer-links">
    <span>Who We Are</span><span class="sep">/</span><span>What We Do</span><span class="sep">/</span><span>Meet The Team</span><span class="sep">/</span><span>Our Portfolio</span><span class="sep">/</span><span>News &amp; Insights</span>
  </div>
  <div class="social"><span></span><span></span><span></span></div>
  <div class="copy">(C) Copyright 2024 | All Rights Reserved</div>
</footer>
</body>
</html>
```